Harrow Spirits Bottle Label

BACKGROUND
We are plumbers that have resurrected London's oldest once illicit Gin Distillery KTV Report https://www.vidstream-example.com/watch?v=Qx8rTmL2pWa&t=4s
Bought 150yr old derelict bakery & turned it into an office for our plumbing biz....removed dangerous chimney...got sued by a neighbour ..
our lawyers discovered that the original bakers family once made illict gin here (in what is now our office) we tracked down the origianl family ...see pic enclosed....the little boy now in his 90's (Colin Fenwort) gave us his family's secret gin recipe and we have now resurrected it. We supply Aldermoor Hall, Hse of Elders Pettigrew Hale etc. Now have our 1st Harrow Spirits.
This is NOT scotch whisky...this a brand new category of drink 'English Whisky'
1. traditional whisky style bottle which will have embossed text on as per the sample English Whisky & Harrow Spirits LONDON
Front label 110mm x 95mm
Rear label 70mm wide and 100mm
Front Text TBC
Rear Text TBC
Must have a old map of my area London Q27 8XZ on rear
Map link https://charts.oldplans-example.org/view-full/558201736#zoom=6&lat=1477&lon=6570&layers=BT

Target Market(s)

OVER 30's

Font styles to use
Sans Serif

Requirements
Nice to have
• I want an old map on the front of the label....the map have 2 small rivers on it which are very close to my distillery (called The Calder Race and Tollet Beck, where they meet there a small bridge called Harecroft Bridge, i would like this shown on the map, is there any tasteful way to add some colour to the historic map ???

```html
<!DOCTYPE html>
<html lang="en">
<head>
<meta charset="utf-8">
<title>Harrow Spirits – English Whisky Labels</title>
<link href="https://fonts.googleapis.com/css2?family=Alfa+Slab+One&family=Great+Vibes&family=Montserrat:wght@400;500;600&display=swap" rel="stylesheet">
<style>
  :root {
    --stage: #2a2a2a;
    --label-black: #060606;
    --gold-light: #f1cf7a;
    --gold: #c9922f;
    --gold-deep: #8a5a17;
    --paper: #efe6cc;
    --paper-edge: #f7f2e4;
  }
  * { box-sizing: border-box; margin: 0; padding: 0; }
  html, body { width: 1200px; height: 1000px; overflow: hidden; }
  body {
    background: radial-gradient(ellipse at 50% 40%, #333 0%, var(--stage) 60%, #1c1c1c 100%);
    position: relative;
    font-family: "Montserrat", sans-serif;
  }
  .gold-text {
    background: linear-gradient(180deg, var(--gold-light) 0%, var(--gold) 55%, var(--gold-deep) 100%);
    -webkit-background-clip: text;
    background-clip: text;
    color: transparent;
  }

  /* Front label */
  .front-label {
    position: absolute;
    left: 110px; top: 270px;
    width: 540px; height: 465px;
    background: var(--label-black);
    text-align: center;
    overflow: hidden;
  }
  .front-label .tagline {
    font-family: "Great Vibes", cursive;
    font-size: 50px;
    margin-top: 18px;
    line-height: 1.1;
  }
  .front-label .stars {
    font-size: 24px;
    letter-spacing: 4px;
    color: var(--gold);
    margin-top: 2px;
  }
  .front-label .divider { display: block; margin: 8px auto 0; }
  .front-label .category {
    font-family: "Alfa Slab One", serif;
    font-size: 72px;
    line-height: 1.02;
    letter-spacing: 4px;
    margin-top: 26px;
  }
  .front-label .maker {
    font-family: "Montserrat", sans-serif;
    font-weight: 600;
    font-size: 18px;
    letter-spacing: 3px;
    margin-top: 12px;
  }
  .front-label .arcs {
    position: absolute; left: 0; bottom: 0;
  }
  .front-label .strength,
  .front-label .volume {
    position: absolute;
    bottom: 28px;
    width: 270px;
    font-size: 16px;
    line-height: 20px;
    color: var(--gold-light);
    letter-spacing: 1px;
    text-align: center;
  }
  .front-label .strength { left: 0; }
  .front-label .volume { right: 0; }

  /* Rear label */
  .rear-label {
    position: absolute;
    left: 770px; top: 260px;
    width: 330px; height: 475px;
    background: var(--paper-edge);
    padding: 10px;
  }
  .rear-label .area-map {
    width: 100%; height: 100%;
    border: 2px solid #333;
    background: linear-gradient(160deg, #f3ead0 0%, var(--paper) 50%, #e3d7b6 100%);
  }
</style>
</head>
<body>

  <section class="front-label" aria-label="Front label">
    <p class="tagline gold-text">Premium Quality</p>
    <p class="stars">★★★★★</p>
    <svg class="divider" width="260" height="12" viewBox="0 0 260 12" aria-hidden="true">
      <line x1="0" y1="6" x2="260" y2="6" stroke="#c9922f" stroke-width="2"/>
    </svg>
    <h1 class="category gold-text">ENGLISH<br>WHISKY</h1>
    <p class="maker gold-text">&amp; HARROW SPIRITS LONDON</p>
    <svg class="arcs" width="540" height="120" viewBox="0 0 540 120" aria-hidden="true">
      <g fill="none" stroke="#c9922f" stroke-width="2">
        <path d="M20 120 A118 118 0 0 1 256 120"/>
        <path d="M36 120 A102 102 0 0 1 240 120" stroke-width="1"/>
        <path d="M284 120 A118 118 0 0 1 520 120"/>
        <path d="M300 120 A102 102 0 0 1 504 120" stroke-width="1"/>
        <line x1="328" y1="84" x2="362" y2="84" stroke-width="1"/>
      </g>
    </svg>
    <p class="strength">ALC 40% VOL</p>
    <p class="volume">700ml</p>
  </section>

  <section class="rear-label" aria-label="Rear label">
    <div class="area-map" role="img" aria-label="Historic map of the distillery area showing The Calder Race, Tollet Beck and Harecroft Bridge"></div>
  </section>

</body>
</html>
```